Skin Care business card for esthetician that is home based

I need a business card for my esthetician business. I would like to use a picture provided.
I want the picture #1 that I have provided to be as the main background with my title and the moto underneath in smaller lettering. Below that as a seperate thing I would like my full name and underneath in small letters to say "esthetician".
As a seperate paragraph I would like my address then phone number, email and my website that I have provided in the business card details.
On the back side I would like my second picture to be small and in the top left corner and then have the "nice to haves" details to be at the center bottom of the card.
Target Market(s)
mosty women between 18 and 60 years old
Industry/Entity Type
Skin Care
Contact Information for Business Card
Velvet Bloom Skin Care - Main Title
Helping you find beautiful! - motto
Marisol Teodora Vinchek -
Phone: 314.827.5093
7382 SW 9th Avenue
Oakvale WA 98472
oakvaleskincare@mailhaven.example
www.oakvaleskincare.example
Must have
- Picure I provided or other similar photo.
Nice to have
- On the back side:
Helping you find beautiful!
www.oakvaleskincare.example

```html
<!DOCTYPE html>
<html lang="en">
<head>
<meta charset="utf-8">
<title>Velvet Bloom Skin Care – Business Card</title>
<link rel="stylesheet" href="https://fonts.googleapis.com/css2?family=Marcellus&family=PT+Sans&display=swap">
<style>
  :root {
    --page: #ffffff;
    --cream: #f6efe7;
    --brown: #5b2f1f;
    --brown-soft: #6e3b27;
    --ink: #3a1d12;
    --white: #ffffff;
    --skin-1: #e9d6c6;
    --skin-2: #c9a58a;
    --petal-1: #fbf3ec;
    --petal-2: #f3d6cc;
  }
  * { box-sizing: border-box; margin: 0; padding: 0; }
  html, body { width: 1030px; height: 1200px; overflow: hidden; background: var(--page); }
  body { position: relative; font-family: "PT Sans", sans-serif; color: var(--ink); }

  .card {
    position: absolute;
    left: 64px;
    width: 902px;
    height: 524px;
    overflow: hidden;
    background: var(--cream);
    box-shadow: 0 2px 8px rgba(0,0,0,0.18);
  }
  .card--front { top: 36px; }
  .card--back  { top: 604px; }

  /* Front */
  .spa-photo {
    position: absolute; inset: 0;
    background: linear-gradient(100deg, var(--skin-2) 0%, var(--skin-1) 35%, var(--cream) 62%, var(--cream) 100%);
  }
  .brand-shapes { position: absolute; inset: 0; }

  .identity {
    position: absolute; right: 34px; top: 22px;
    text-align: right;
    font-family: "Marcellus", serif;
  }
  .identity__title { font-size: 37px; font-weight: 400; color: var(--brown-soft); line-height: 1.2; }
  .identity__motto { font-size: 23px; color: var(--brown-soft); margin-top: 2px; }
  .identity__name  { font-size: 25px; color: var(--ink); margin-top: 16px; }
  .identity__role  { font-size: 18px; color: var(--ink); text-align: center; margin-top: 2px; padding-left: 60px; }

  .contact {
    position: absolute; left: 684px; top: 278px;
    color: var(--white); font-size: 23px; line-height: 1.35;
  }
  .contact__icon { display: block; width: 26px; height: 30px; margin: 0 0 6px 62px; }
  .contact__phone { margin-bottom: 14px; }
  .contact__address { font-style: normal; }

  .footer-band {
    position: absolute; left: 0; right: 0; bottom: 0; height: 73px;
    color: var(--white); font-size: 23px;
  }
  .footer-band__item { display: flex; align-items: center; gap: 12px; position: absolute; top: 50%; transform: translateY(-50%); }
  .footer-band__item svg { width: 28px; height: 28px; }
  .footer-band__email { left: 54px; }
  .footer-band__web   { left: 556px; }

  /* Back */
  .petal-backdrop {
    position: absolute; inset: 0;
    background: radial-gradient(ellipse at 80% 55%, var(--petal-2) 0%, var(--petal-1) 55%, var(--cream) 100%);
  }
  .portrait {
    position: absolute; left: 0; top: 0; width: 396px; height: 100%;
    background: linear-gradient(180deg, #cfb79c 0%, #e6d8c8 45%, #f2ece6 100%);
  }
  .back-motto {
    position: absolute; left: 410px; top: 212px;
    font-family: "Marcellus", serif; font-size: 37px; color: var(--brown-soft);
  }
  .back-band {
    position: absolute; left: 367px; right: 0; bottom: 0; height: 71px;
    background: var(--brown);
    display: flex; align-items: center; gap: 14px;
    padding-left: 96px;
    color: var(--white); font-size: 23px;
  }
  .back-band svg { width: 28px; height: 28px; }
</style>
</head>
<body>

<section class="card card--front">
  <div class="spa-photo" role="img" aria-label="Photo of a woman receiving a relaxing facial treatment with spa stones and a candle"></div>

  <svg class="brand-shapes" width="902" height="524" viewBox="0 0 902 524" aria-hidden="true">
    <polygon points="842,202 902,262 902,451 490,451" fill="var(--brown)"/>
    <rect x="0" y="451" width="902" height="73" fill="var(--brown)"/>
  </svg>

  <div class="identity">
    <h1 class="identity__title">Velvet Bloom Skin Care</h1>
    <p class="identity__motto">Helping you find beautiful!</p>
    <p class="identity__name">Marisol Teodora Vinchek</p>
    <p class="identity__role">“esthetician”</p>
  </div>

  <div class="contact">
    <svg class="contact__icon" viewBox="0 0 24 24" aria-hidden="true">
      <path fill="var(--white)" d="M6.6 2.5c.6-.3 1.3-.1 1.6.5l1.7 3.4c.3.6.1 1.2-.3 1.6L8.3 9.3c1 2.4 3.9 5.3 6.4 6.4l1.3-1.3c.4-.4 1.1-.6 1.6-.3l3.4 1.7c.6.3.8 1 .5 1.6l-1 2c-.5 1-1.6 1.5-2.6 1.3C9.9 19.4 4.6 14.1 3.3 6.1c-.2-1 .3-2.1 1.3-2.6z"/>
    </svg>
    <p class="contact__phone">314.827.5093</p>
    <svg class="contact__icon" viewBox="0 0 24 28" aria-hidden="true">
      <path fill="var(--white)" d="M12 1a8 8 0 0 0-8 8c0 6 8 13 8 13s8-7 8-13a8 8 0 0 0-8-8zm0 11a3 3 0 1 1 0-6 3 3 0 0 1 0 6z"/>
      <ellipse cx="12" cy="25" rx="7" ry="2" fill="none" stroke="var(--white)" stroke-width="1.5"/>
    </svg>
    <address class="contact__address">
      7382 SW 9th Avenue<br>Oakvale WA 98472
    </address>
  </div>

  <div class="footer-band">
    <div class="footer-band__item footer-band__email">
      <svg viewBox="0 0 28 28" aria-hidden="true">
        <rect x="2" y="6" width="24" height="16" fill="var(--white)"/>
        <path d="M2 6l12 9 12-9" fill="none" stroke="var(--brown)" stroke-width="2"/>
      </svg>
      <span>oakvaleskincare@mailhaven.example</span>
    </div>
    <div class="footer-band__item footer-band__web">
      <svg viewBox="0 0 28 28" aria-hidden="true">
        <circle cx="14" cy="14" r="12" fill="var(--white)"/>
        <g fill="none" stroke="var(--brown)" stroke-width="1.4">
          <ellipse cx="14" cy="14" rx="5" ry="12"/>
          <path d="M2 14h24M4 8h20M4 20h20"/>
        </g>
      </svg>
      <span>oakvaleskincare.example</span>
    </div>
  </div>
</section>

<section class="card card--back">
  <div class="petal-backdrop" role="img" aria-label="Soft pink rose petals scattered on a cream background"></div>
  <div class="portrait" role="img" aria-label="Portrait of the esthetician in a white salon tunic"></div>

  <p class="back-motto">Helping you find beautiful!</p>

  <div class="back-band">
    <svg viewBox="0 0 28 28" aria-hidden="true">
      <circle cx="14" cy="14" r="12" fill="var(--white)"/>
      <g fill="none" stroke="var(--brown)" stroke-width="1.4">
        <ellipse cx="14" cy="14" rx="5" ry="12"/>
        <path d="M2 14h24M4 8h20M4 20h20"/>
      </g>
    </svg>
    <span>www.oakvaleskincare.example</span>
  </div>
</section>

</body>
</html>
```